Looking for a cool, modern Cannabis Jar Label

I want you to come up with a better, modern look for a label.

I need it sized to 4” x 3” - I plan to print directly to label printer.

I want you to use Photoshop and deliver me a layered PSD file that I can edit and modify the information as needed..

The label information will need to include places for:
(1) Strain Name - most important part of label - larger font size than rest - example Kelvin Thistle, TRP #7, Copperleaf Dunes
(2) Pricing - for Gram, 1/8, 1/4, 1/2. and Ounce
(3) Strain Designation (Hybrid, Indica or Sativa) - maybe color coded, different color for Indica v. Sativa, just an idea
(4) THC and CBD percentages - for example 23% THC and 0.05% CBD
(5) Farm name - a place where we can add the name/logo of the business that produced the product. example - Brosk Farms

I have attached a simple mockup showing the information.

I have also attached a few samples of labels we like to give you an idea of the look and feel we are going for.

I am wanting a very clean, modern, classy, readable look.The font will use is Gotham Font.

HI Everyone! Thank you for all of your designs. I am requesting an extension because I need more time to give adequate feedback to the designers. Thank you for your participation and all of your efforts! I will be making a decision soon!

• Gotham Font

• Thank you for your designs. I am sorry i have been slow in providing feedback, things have been really busy around here!
• I wanted to give some group general feedback. After reviewing all of the designs, there is a common theme among all of the designs that I would like to see changed.
• I would like to see the per gram pricing more prominent on the label. This is what most people are looking for when they are purchasing the product. So I would like to see this stand out from the other pricing tiers. As I think about it, they don't all need to be grouped together in a line. You could have the Per Gram pricing front and center some where and then the other pricing tiers grouped together somewhere else on the label.
• This is the order of importance of items on the label. Items at the the top of the list should be bigger than those below it.
• 1. Strain name
• 2. Pricing - being per gram the most important of all prices
• 3. THC/CBD percentages
• 4. Strain Type (indica, sativa, hybrid)
• 5. Farm name/logo
• When laying out these labels, they will be going on rounded jars and they will be on display. Think of jars with fancy labels in a candy store. They need to be eye catchy, appealing, but easy read.
• Thank you for all of your hard work, everyone is doing a great job.
• Best,
• Neta

```html
<!DOCTYPE html>
<html lang="en">
<head>
<meta charset="utf-8">
<title>Marlow Creek Frost – Jar Label</title>
<link href="https://fonts.googleapis.com/css2?family=Montserrat:wght@400;500;600;700&display=swap" rel="stylesheet">
<style>
  :root {
    --navy: #2d2e7f;
    --mint: #94d3ce;
    --teal: #4ec0b8;
    --pale: #cdebea;
    --leaf-a: #7cc9c9;
    --leaf-b: #a6dcd8;
  }
  * { margin: 0; padding: 0; box-sizing: border-box; }
  html, body { width: 1200px; height: 900px; overflow: hidden; background: #ffffff; }
  .label {
    position: relative; width: 1200px; height: 900px; overflow: hidden;
    font-family: "Montserrat", "Helvetica Neue", Arial, sans-serif;
    color: var(--navy);
  }
  .band-top { position: absolute; left: 0; top: 0; width: 1200px; height: 373px; background: var(--navy); }
  .panel-farm { position: absolute; left: 0; top: 373px; width: 381px; height: 527px; background: var(--mint); }
  .panel-stats { position: absolute; left: 381px; top: 373px; width: 819px; height: 527px; background: var(--teal); }
  .price-disc { position: absolute; left: 0; top: 0; width: 1200px; height: 900px; }

  .strain-name {
    position: absolute; left: 133px; top: 95px; max-width: 630px;
    font-size: 70px; font-weight: 700; line-height: 94px; letter-spacing: 0;
    color: var(--mint); text-transform: uppercase; white-space: nowrap;
  }
  .farm-name {
    position: absolute; left: 95px; top: 532px; width: 205px; text-align: center;
    font-size: 41px; font-weight: 400; line-height: 53px; text-transform: uppercase;
  }
  .potency { position: absolute; right: 516px; top: 429px; text-align: right; font-weight: 700; font-size: 62px; line-height: 88px; }
  .potency sup { font-size: 28px; vertical-align: 26px; margin-right: 14px; }
  .strain-type {
    position: absolute; left: 413px; top: 734px;
    font-size: 50px; font-weight: 600; text-decoration: underline;
    text-decoration-thickness: 3px; text-underline-offset: 8px;
  }
  .tier { position: absolute; left: 884px; width: 300px; height: 138px; display: flex; align-items: center; }
  .tier-price {
    width: 138px; height: 138px; border-radius: 50%; background: var(--pale);
    display: flex; align-items: center; justify-content: center;
    font-size: 50px; font-weight: 600; letter-spacing: -1px; color: var(--navy);
  }
  .tier-price sup { font-size: 26px; vertical-align: 20px; margin-right: 2px; }
  .tier-unit { margin-left: 18px; font-size: 23px; font-weight: 700; }
  .tier--gram .tier-price { background: var(--navy); color: var(--pale); font-size: 62px; }
  .tier--gram .tier-price sup { font-size: 30px; vertical-align: 26px; }
  .tier--gram .tier-unit { font-size: 31px; }
</style>
</head>
<body>
<div class="label">
  <div class="band-top"></div>
  <div class="panel-farm"></div>
  <div class="panel-stats"></div>

  <svg class="price-disc" viewBox="0 0 1200 900" role="img" aria-label="Soft watercolour leaf texture inside the pricing circle">
    <defs>
      <radialGradient id="leafWash" cx="0.55" cy="0.55" r="0.6">
        <stop offset="0" stop-color="#7cc9c9"/>
        <stop offset="1" stop-color="#a6dcd8"/>
      </radialGradient>
    </defs>
    <circle cx="1168" cy="450" r="463" fill="#94d3ce"/>
    <circle cx="1168" cy="450" r="463" fill="url(#leafWash)" opacity="0.55"/>
  </svg>

  <h1 class="strain-name">Marlow Creek<br>Frost</h1>

  <div class="farm-name">Farm<br>Logo<br>Goes<br>Here</div>

  <div class="potency">
    <div>28<sup>%</sup>THC</div>
    <div>2<sup>%</sup>CBD</div>
  </div>

  <div class="strain-type">INDICA</div>

  <div class="tier tier--gram" style="top:99px"><div class="tier-price"><sup>$</sup>10</div><span class="tier-unit">GRAM</span></div>
  <div class="tier" style="top:241px"><div class="tier-price"><sup>$</sup>35</div><span class="tier-unit">1/8 OZ</span></div>
  <div class="tier" style="top:386px"><div class="tier-price"><sup>$</sup>70</div><span class="tier-unit">1/4 OZ</span></div>
  <div class="tier" style="top:529px"><div class="tier-price"><sup>$</sup>140</div><span class="tier-unit">1/2 OZ</span></div>
  <div class="tier" style="top:671px"><div class="tier-price"><sup>$</sup>280</div><span class="tier-unit">OUNCE</span></div>
</div>
</body>
</html>
```